Kestrel Signs Facebook Banner Design

Design a facebook banner for a sign company. I would like to have a modern approach to it.

Product Offering:
Signs
Banners
Decals
Commercial Wraps

```html
<!DOCTYPE html>
<html lang="en">
<head>
<meta charset="utf-8">
<title>Kestrel Signs – Facebook Banner</title>
<link rel="stylesheet" href="https://fonts.googleapis.com/css2?family=Russo+One&family=Exo+2:wght@500&display=swap">
<style>
  :root {
    --page: #f3f4f3;
    --panel: #3a3d40;
    --red: #e8303a;
    --frame-red: #e0221c;
    --white: #ffffff;
    --tile: #5b5857;
    --pill-edge: #e42a1f;
    --pill-mid: #f7a20c;
    --pill-core: #ffe600;
    --photo-top: #e4ebf2;
    --photo-mid: #2f5fa8;
    --photo-low: #7a1418;
  }
  * { margin: 0; padding: 0; box-sizing: border-box; }
  html, body {
    width: 1200px; height: 1200px; overflow: hidden;
    background: var(--page);
  }
  .canvas { position: relative; width: 1200px; height: 1200px; }
  .banner {
    position: absolute; left: 40px; top: 393px;
    width: 1120px; height: 414px;
    background: var(--panel);
    overflow: hidden;
  }
  .banner-art { position: absolute; inset: 0; width: 1120px; height: 414px; }
  .brand {
    font-family: "Russo One", sans-serif;
    text-transform: uppercase;
    font-weight: 400;
  }
  .brand-line {
    position: absolute; left: 87px; width: 563px;
    text-align: center; line-height: 1; white-space: nowrap;
  }
  .brand-main { top: 33px; font-size: 96px; letter-spacing: 8px; color: var(--red); }
  .brand-sub { top: 115px; font-size: 74px; letter-spacing: 6px; color: var(--white); }
  .offer-pill {
    position: absolute; left: 220px; top: 211px;
    width: 280px; height: 38px; border-radius: 19px;
    background: linear-gradient(90deg, var(--pill-edge) 0%, var(--pill-mid) 35%, var(--pill-core) 50%, var(--pill-mid) 65%, var(--pill-edge) 100%);
    color: var(--white);
    font-family: "Exo 2", sans-serif; font-weight: 500;
    font-size: 21px; letter-spacing: 3px;
    display: flex; align-items: center; justify-content: center;
    white-space: nowrap;
  }
  .offer-list {
    position: absolute; left: 0; width: 722px;
    display: flex; justify-content: center; gap: 24px;
    list-style: none;
    font-family: "Exo 2", sans-serif; font-weight: 500;
    font-size: 36px; letter-spacing: 2px;
    color: var(--white); line-height: 1; white-space: nowrap;
  }
  .offer-list li { display: flex; align-items: center; }
  .offer-list li::before {
    content: ""; display: inline-block;
    width: 3px; height: 26px; background: var(--red);
    margin-right: 8px;
  }
  .offer-list.row-one { top: 277px; }
  .offer-list.row-two { top: 338px; left: 10px; }
</style>
</head>
<body>
<main class="canvas">
  <section class="banner">
    <svg class="banner-art" viewBox="0 0 1120 414">
      <defs>
        <linearGradient id="workFill" x1="0" y1="0" x2="0" y2="1">
          <stop offset="0" stop-color="var(--photo-top)"/>
          <stop offset="0.5" stop-color="var(--photo-mid)"/>
          <stop offset="1" stop-color="var(--photo-low)"/>
        </linearGradient>
        <clipPath id="frameClip">
          <path d="M805 37 L996 39 L870 170 Q858 186 872 200 L1069 380 L895 382 L693 225 Q680 212 693 198 Z"/>
        </clipPath>
      </defs>
      <g class="tiles" fill="var(--tile)">
        <rect x="94" y="181" width="12" height="12" rx="2"/>
        <rect x="109" y="181" width="12" height="12" rx="2"/>
        <rect x="94" y="196" width="12" height="12" rx="2"/>
        <rect x="109" y="196" width="12" height="12" rx="2"/>
        <rect x="564" y="155" width="11" height="11" rx="2"/>
        <rect x="578" y="155" width="11" height="11" rx="2"/>
        <rect x="564" y="169" width="11" height="11" rx="2"/>
        <rect x="578" y="169" width="11" height="11" rx="2"/>
        <rect x="965" y="108" width="42" height="47" rx="5"/>
        <rect x="1023" y="108" width="42" height="47" rx="5"/>
        <rect x="965" y="172" width="42" height="47" rx="5"/>
        <rect x="1023" y="172" width="42" height="47" rx="5"/>
        <rect x="662" y="343" width="44" height="39" rx="5"/>
        <rect x="722" y="343" width="44" height="39" rx="5"/>
        <rect x="662" y="395" width="44" height="39" rx="5"/>
        <rect x="722" y="395" width="44" height="39" rx="5"/>
      </g>
      <path class="work-showcase" role="img" aria-label="Photo collage of finished work: a wrapped van, storefront signs and a sale banner"
            clip-path="url(#frameClip)" fill="url(#workFill)"
            d="M802 56 L960 56 L850 175 Q840 190 854 204 L1025 366 L895 366 L724 216 Q712 203 722 190 Z"/>
      <path class="chevron-frame" fill="none" stroke="var(--frame-red)" stroke-width="4" stroke-linejoin="round"
            d="M805 37 L996 39 L870 170 Q858 186 872 200 L1069 380 L895 382 L693 225 Q680 212 693 198 Z"/>
    </svg>

    <h1 class="brand">
      <span class="brand-line brand-main">Kestrel</span>
      <span class="brand-line brand-sub">Signs</span>
    </h1>

    <div class="offer-pill">PRODUCT OFFERING</div>

    <ul class="offer-list row-one">
      <li>SIGNS</li>
      <li>BANNERS</li>
      <li>DECALS</li>
    </ul>
    <ul class="offer-list row-two">
      <li>COMMERCIAL WRAPS</li>
    </ul>
  </section>
</main>
</body>
</html>
```